High-End Medical Center Website Design Project

This design is part of a well thought-out project by an experienced project manager / developer. The approved wireframe is attached. Creative interpretations / suggestions based on the layout encouraged.

The design is for a new state-of-the-art medical center located in Dallas, Texas. The target audience would likely be individuals (approx. 60% female /40% male) who are the healthcare decision-makers for their families. They would likely have insurance and be inclined to seek out top-quality care.

Potential clients would choose this client over others in their industry because the medical center is physician owned, meaning it is patient-focused rather than profit-focused. The facility is brand new, featuring the latest technology. (This includes an amazing waiting room featuring WiFi and docking stations.) The physicians are hand-picked by referral only.

The look of the site should be extremely clean. We are going for a well-organized, professional look with a bit of a warm glow (interpret that however you like). Use crisp corners and the colors in the logo.

Think modern, clean with some great use of color / font.

We can get lovely photography of the medical center once construction is complete. Feel free to use an "example image" behind the Featured Area ("Physician Owned. Patient-Focused") if you like. We are open to ideas.

ONE CHANGE REQUESTED IN THE WIREFRAME:

Remove the "Connect" 1/4 page footer area and replace with a quick contact form. You may swap the "Locations" area with the form if desired. Put social media icons at the top left of the page in the top header area.

(Note: Please use social media icons that match the design rather than standard icons. We preferred not placing the icons at the top, but the client requested this. Let's not bring more attention to them than necessary.)
Updates

We're custom programming this site, so there's no need to base it on a template. Also, we would prefer not to use typical "seen everywhere" stock images.Thanks.

Industry/Entity Type

Construction

Requirements
Must have
• Follow the wireframe. This has been approved.
Nice to have
• Examples of what hover states, links or dropdowns might look like.

```html
<!DOCTYPE html>
<html lang="en">
<head>
<meta charset="utf-8">
<title>Lumen Medical Center</title>
<link rel="stylesheet" href="https://fonts.googleapis.com/css2?family=Arimo:ital,wght@0,400;0,700;1,400&display=swap">
<style>
:root{
  --dark:#2b2b2b;
  --darker:#232323;
  --brand:#0d5aa7;
  --brand-deep:#0b4c8f;
  --teal:#2e8f8c;
  --steel:#6a9fb5;
  --steel-box:#6b9fb4;
  --text:#666;
  --muted:#888;
  --line:#dcdcdc;
  --panel:#f4f4f4;
  --white:#fff;
}
*{margin:0;padding:0;box-sizing:border-box}
html,body{width:920px;height:1200px;overflow:hidden}
body{font-family:"Arimo",Arial,sans-serif;color:var(--text);background:var(--white);position:relative}
.abs{position:absolute}

.topbar{left:0;top:0;width:920px;height:35px;background:var(--dark)}
.social{top:8px;width:18px;height:18px;background:#e9e9e9;border-radius:2px}
.callnow{right:68px;top:10px;color:#eee;font-size:12px;font-weight:700;display:flex;align-items:center;gap:6px}

.header{left:0;top:35px;width:920px;height:81px;background:linear-gradient(#fff,#f3f3f3)}
.brand{left:69px;top:23px;display:flex;align-items:center;gap:8px;font-size:20px;font-weight:700;color:var(--brand);letter-spacing:.5px}
.brand .mark{width:26px;height:26px;background:var(--brand)}
.nav{right:69px;top:35px;display:flex;font-size:12px;font-weight:700;color:#333}
.nav span{padding:0 14px;border-left:1px solid #ccc;line-height:16px}
.nav span:first-child{border-left:0}
.nav .active{color:var(--brand);position:relative}
.nav .active:after{content:"";position:absolute;left:14px;right:14px;bottom:-6px;height:2px;background:var(--brand)}

.hero{left:0;top:116px;width:920px;height:297px;background:linear-gradient(90deg,#14569c,#2270b8 50%,#175c9f)}
.hero h1{position:absolute;left:0;width:920px;top:36px;text-align:center;color:#fff;font-size:27px;font-weight:700}
.hero p{position:absolute;left:175px;width:570px;top:74px;text-align:center;color:#eef;font-size:12.3px;line-height:20.7px}
.hero .rule{position:absolute;left:140px;width:640px;top:160px;height:1px;background:rgba(255,255,255,.25)}
.arrow{width:32px;height:32px;border-radius:50%;background:#fff;top:131px;display:flex;align-items:center;justify-content:center}
.feature{width:80px;height:80px;border-radius:50%;background:radial-gradient(#fff 55%,#e4e9ee);top:188px}

.apart{left:0;top:413px;width:920px;height:203px;border-bottom:1px solid var(--line)}
.apart h2{position:absolute;left:71px;top:50px;font-size:21px;color:var(--brand);line-height:26px}
.apart .divider{position:absolute;left:185px;top:32px;width:1px;height:140px;background:#e2e2e2}
.col{top:54px;width:200px}
.col h3{font-size:16px;font-weight:400;color:var(--steel);margin-bottom:12px}
.col p{font-size:10.4px;line-height:17.6px;color:var(--text)}
.more{font-size:10.4px;color:var(--brand)}
.more:after{content:"";display:inline-block;margin-left:6px;border-left:4px solid var(--brand);border-top:3px solid transparent;border-bottom:3px solid transparent}

.about{left:0;top:616px;width:920px;height:295px;background:var(--panel);border-bottom:1px solid var(--line)}
.photo{left:70px;top:50px;width:168px;height:196px;border:1px solid #ddd;background:linear-gradient(90deg,#7fa3c6,#dfe7ef 55%,#f5f5f5)}
.about h3{position:absolute;left:265px;top:50px;font-size:16px;color:var(--teal)}
.about .body{position:absolute;left:265px;top:80px;width:324px;font-size:10.4px;line-height:17.6px;text-align:justify}
.testi-h{left:616px;top:17px;font-size:16px;font-weight:700;color:var(--teal)}
.quote{left:616px;top:49px;width:235px;height:199px;background:#fff;border:1px solid #e2e2e2;padding:20px 12px 0 24px;font-style:italic;font-size:10.4px;line-height:19.2px;text-align:justify}
.client{left:717px;top:269px;font-size:11px;color:var(--teal)}

.boxhead{top:934px;width:173px;height:28px;border:1px solid #d8d8d8;background:linear-gradient(#fff,#f1f1f1);font-size:13px;font-weight:700;color:#333;padding:7px 14px}
.boxhead .go{position:absolute;right:12px;top:7px;width:14px;height:14px;border:1px solid #ccc;background:#fff}
.list{top:978px;width:170px;font-size:9.6px;line-height:12.8px;color:var(--text)}
.list li{list-style:none;padding-left:15px;position:relative;margin-bottom:16px}
.list li:before{content:"";position:absolute;left:3px;top:3px;border-left:3px solid #aaa;border-top:3px solid transparent;border-bottom:3px solid transparent}
.list .date{display:block;margin-top:5px;font-size:8.5px;color:#333}
.field{left:482px;width:161px;height:22px;border:1px solid #ccc;background:#fff;font-size:8.5px;color:#999;padding:6px 11px}
.submit{left:590px;top:1110px;width:53px;height:21px;background:linear-gradient(#aaa,#888);color:#fff;font-size:10.5px;font-weight:700;text-align:center;line-height:21px}
.wait{left:679px;top:934px;width:173px;height:196px;background:var(--steel-box);border:1px solid #5a8ea4;color:#fff;text-align:center}
.wait .t1{position:absolute;top:82px;width:100%;font-size:14px;font-weight:700}
.wait .t2{position:absolute;top:103px;width:100%;font-size:19px;font-weight:700}
.wait .t3{position:absolute;top:132px;width:100%;font-size:9.6px;font-weight:700;line-height:14.5px;padding:0 14px}

.footer{left:0;top:1152px;width:920px;height:48px;background:var(--darker);border-top:2px solid #444;color:#bbb;font-size:11px}
.footer .copy{position:absolute;left:70px;top:17px}
.footer .links{position:absolute;right:68px;top:17px}
</style>
</head>
<body>

<div class="abs topbar">
  <div class="abs social" style="left:70px"></div>
  <div class="abs social" style="left:97px"></div>
  <div class="abs social" style="left:124px"></div>
  <div class="abs social" style="left:151px"></div>
  <div class="abs callnow">
    <svg width="12" height="12" viewBox="0 0 24 24"><path fill="#ccc" d="M6.6 10.8a15 15 0 0 0 6.6 6.6l2.2-2.2c.3-.3.7-.4 1-.2 1.1.4 2.3.6 3.6.6.6 0 1 .4 1 1V20c0 .6-.4 1-1 1A17 17 0 0 1 3 4c0-.6.4-1 1-1h3.5c.6 0 1 .4 1 1 0 1.3.2 2.5.6 3.6.1.3 0 .7-.2 1z"/></svg>
    Call now : (555) 014 2270
  </div>
</div>

<div class="abs header">
  <div class="abs brand"><span class="mark"></span>LUMEN MEDICAL CENTER</div>
  <nav class="abs nav">
    <span class="active">Why Lumen</span><span>Physicians</span><span>Specialities</span><span>Info</span><span>Locations</span><span>Contact</span>
  </nav>
</div>

<section class="abs hero" role="img" aria-label="Blue-tinted photograph of a hospital corridor">
  <h1>Physician Owned. Patient Focused</h1>
  <p>Nulla imperdiet sodales nisi, sed lacinia justo facilisis nec. Nunc a lacus sit amet purus vestibulum faucibus. In nibh tortor, fringilla at ligula quis, tincidunt molestie nunc. Maecenas nec eros nibh. Nunc a auctor magna. Proin quis quam eu libero tempus vehicula. Donec lacinia dolor a risus eleifend.</p>
  <div class="rule"></div>
  <div class="abs arrow" style="left:68px"><svg width="12" height="12" viewBox="0 0 12 12"><path d="M8 1 3 6l5 5" stroke="#999" fill="none" stroke-width="1.3"/></svg></div>
  <div class="abs arrow" style="left:819px"><svg width="12" height="12" viewBox="0 0 12 12"><path d="M4 1l5 5-5 5" stroke="#999" fill="none" stroke-width="1.3"/></svg></div>
  <div class="abs feature" style="left:282px" role="img" aria-label="Doctor illustration"></div>
  <div class="abs feature" style="left:436px" role="img" aria-label="Notepad and pencil illustration"></div>
  <div class="abs feature" style="left:590px" role="img" aria-label="Question mark illustration"></div>
</section>

<section class="abs apart">
  <h2>What sets<br>us Apart</h2>
  <div class="divider"></div>
  <div class="abs col" style="left:216px"><h3>Technology</h3><p>Aliquam aliquet, lorem et euismod tempor, ipsum massa vulputate metus, elementum iaculis sapien ipsum eget mauris</p><p class="more" style="margin-top:14px">Know more</p></div>
  <div class="abs col" style="left:438px"><h3>Quality of care</h3><p>Aliquam aliquet, lorem et euismod tempor, ipsum massa vulputate metus, elementum iaculis sapien ipsum eget mauris</p><p class="more" style="margin-top:14px">Know more</p></div>
  <div class="abs col" style="left:658px"><h3>Patient Experience</h3><p>Aliquam aliquet, lorem et euismod tempor, ipsum massa vulputate metus, elementum iaculis sapien ipsum eget mauris</p><p class="more" style="margin-top:14px">Know more</p></div>
</section>

<section class="abs about">
  <div class="abs photo" role="img" aria-label="Photo of a smiling doctor with a stethoscope and colleagues behind"></div>
  <h3>About Lumen Medical Center</h3>
  <p class="body">Curabitur elementum dui at vestibulum vulputate. Quisque sit amet est rhoncus, condimentum lorem et, volutpat urna. Suspendisse faucibus, leo eget pulvinar blandit, massa quam consequat eros, id aliquam lectus velit ac massa. Nulla hendrerit ipsum mauris, blandit tincidunt nibh malesuada id. Aenean vel odio dignissim, iaculis ipsum ullamcorper, hendrerit mi. Etiam quam nulla, tempor sit amet justo mattis, euismod semper orci. .</p>
  <p class="abs more" style="left:266px;top:231px">Know more</p>
  <div class="abs testi-h">Testimonials</div>
  <svg class="abs" style="left:827px;top:19px" width="26" height="10" viewBox="0 0 26 10"><path d="M6 1 2 5l4 4M20 1l4 4-4 4" stroke="#777" fill="none" stroke-width="1.6"/></svg>
  <div class="abs quote"><b style="font-size:16px;color:#888;font-style:normal">“</b> Proin lectus lorem, semper sed nulla quis, congue malesuada elit. Aenean sollicitudin dui vel pharetra mollis. Nullam pulvinar sodales sapien, non convallis odio molestie vehicula. Cras non velit vel lectus feugiat. Fusce commodo lacus ut tellus fringilla, ac dictum nunc gravida. Cras adipiscing, est non molestie auctor <b style="font-size:16px;color:#888;font-style:normal">”</b></div>
  <div class="abs client">Client name, City</div>
</section>

<div class="abs boxhead" style="left:69px">News<span class="go"></span></div>
<ul class="abs list" style="left:69px">
  <li>Nulla facilisi. Curabitur at elit ligula, eget hen drerit felis vehicula.<span class="date">Jul-18-2013</span></li>
  <li>Nulla facilisi. Curabitur at elit ligula, eget hen drerit felis vehicula.<span class="date">Jul-18-2013</span></li>
  <li>Nulla facilisi. Curabitur at elit ligula, eget hen drerit felis vehicula.<span class="date">Jul-18-2013</span></li>
</ul>
<div class="abs boxhead" style="left:272px">Blog<span class="go"></span></div>
<ul class="abs list" style="left:272px">
  <li>Nulla facilisi. Curabitur at elit ligula, eget hen drerit felis vehicula.<span class="date">Jul-18-2013</span></li>
  <li>Nulla facilisi. Curabitur at elit ligula, eget hen drerit felis vehicula.<span class="date">Jul-18-2013</span></li>
  <li>Nulla facilisi. Curabitur at elit ligula, eget hen drerit felis vehicula.<span class="date">Jul-18-2013</span></li>
</ul>
<div class="abs boxhead" style="left:476px">Quick Contact</div>
<div class="abs field" style="top:980px">Name</div>
<div class="abs field" style="top:1013px">Email</div>
<div class="abs field" style="top:1045px">Phone</div>
<div class="abs field" style="top:1077px">Message</div>
<div class="abs submit">SUBMIT</div>

<div class="abs wait">
  <svg class="abs" style="left:61px;top:16px" width="52" height="52" viewBox="0 0 52 52"><circle cx="26" cy="26" r="23" fill="none" stroke="#fff" stroke-width="3"/><path d="M26 10v16l-3-9" stroke="#fff" fill="none" stroke-width="1.6"/></svg>
  <div class="t1">Average wait Time</div>
  <div class="t2">9 Minutes</div>
  <div class="t3">Etiam turpis nisi, condimentum et nulla consectetur, tempus rutrum magna.</div>
</div>

<footer class="abs footer">
  <span class="copy">Copyright © 2013 Lumen Medical Center.</span>
  <span class="links">Sitemap &nbsp; | &nbsp; Privacy</span>
</footer>

</body>
</html>
```